Website Design for Non-profit

We are looking for a new site design for the Patrons of the Northern Heritage Hall. The current site can be found at
http://www.patrons-hall.org/pnhhindex_e.html
The URL is provided for reference. We want a completely different look and layout which is shown in the specifications document. Visiting the site, you can learn more about the organization.
Initially, we would like a home page, and inside page provided. Once we a home page and inside page are selected, we would like a simple mobile template provided.
I have attached a full description of the project as well as the specifications document and a zip file containing images for the site.
As mentioned in the specs document, we want to include an image of the museum in the header. The zip file is too large for us to upload (80 meg). The zip file can be obtained by clicking this link:
http://qzl.cc/TrWpKe
The zip file contains several exterior photos and you can select the one you feel is most appropriate to your design.
Reason: A long weekend is coming up and a few members of the team are unavailable for review.
Reason: Reviewing designs. Should have a decision next week.
Reason: We are discussing the designs and looking to reach a consensus. I will be implementing some designs today or tomorrow. Hopefully final selection will be next week.
Reason: Still reviewing designs. Hope to get a decision soon.
Reason: Working to finalize the design. Very close.
Industry/Entity Type
Museum
Look and feel
Each slider illustrates characteristics of the customer's brand and the style your logo design should communicate.

```html
<!DOCTYPE html>
<html lang="en">
<head>
<meta charset="utf-8">
<title>Patrons of the Northern Heritage Hall</title>
<link href="https://fonts.googleapis.com/css2?family=Open+Sans:wght@300;400&display=swap" rel="stylesheet">
<style>
:root{
  --bg:#e4e4e7;
  --bg-light:#fbfbfc;
  --olive:#a38d36;
  --link:#2a7fb0;
  --tab:#f1f1f2;
  --text:#454545;
  --muted:#777;
  --white:#fff;
  --rule:#cfcfd3;
  --red:#d2382c;
  --blue:#3b5a9a;
}
*{margin:0;padding:0;box-sizing:border-box}
html,body{width:1091px;height:1200px;overflow:hidden}
body{
  font-family:"Open Sans",Arial,sans-serif;
  background:radial-gradient(ellipse 60% 45% at 48% 38%,var(--bg-light),var(--bg) 100%);
}
.page{position:relative;width:1020px;height:1122px;transform:scale(1.0696);transform-origin:0 0}
.abs{position:absolute}
.brand{left:30px;top:40px;display:flex;align-items:center;gap:14px;color:var(--olive);font-size:23px;font-weight:400;width:400px;line-height:1.2}
.brand-mark{width:40px;height:40px;background:var(--olive);flex:none}
.util-nav{right:34px;top:31px;display:flex;font-size:12.5px}
.util-nav a{color:var(--link);text-decoration:none;padding:0 11px;border-left:1px solid var(--rule);line-height:16px}
.util-nav a:first-child{border-left:none}
.util-nav a:last-child{padding-right:0}
.font-size{left:569px;top:164px;font-size:11px;color:var(--muted);display:flex;align-items:baseline;gap:5px}
.font-size a{color:var(--link);text-decoration:none}
.social{top:154px;width:36px;height:36px}
.social.red{left:695px;background:var(--red)}
.social.blue{left:735px;background:var(--blue)}
.search{left:795px;top:155px;width:190px;height:34px;background:var(--white);box-shadow:0 2px 4px rgba(0,0,0,.25)}
.search svg{position:absolute;right:9px;top:9px}
.tabs{display:flex;gap:3px}
.tabs a{display:block;height:50px;line-height:52px;background:var(--tab);color:var(--link);font-weight:300;font-size:15px;text-decoration:none;text-align:center;box-shadow:4px 0 5px -2px rgba(0,0,0,.35)}
.tabs a.active{background:var(--olive);color:var(--white)}
.main-nav{left:30px;top:215px}
.frame{background:var(--white);box-shadow:0 0 10px rgba(0,0,0,.25)}
.hero{left:25px;top:265px;width:965px;height:420px;box-shadow:0 0 14px rgba(0,0,0,.35)}
.hero-photo{left:15px;top:10px;width:940px;height:400px;
  background:linear-gradient(180deg,#f1efe9 0%,#e9e4d8 22%,#6a5c52 36%,#3d474a 55%,#9d958b 72%,#c2b9ab 100%)}
.join-tabs{left:25px;top:717px}
.feature{left:25px;top:767px;width:300px;height:200px}
.feature-photo{left:10px;top:10px;width:280px;height:180px;background:linear-gradient(160deg,#5a8a72,#3f6e5a 60%,#55806a)}
.intro{left:359px;top:786px;width:630px;font-size:11.6px;line-height:17px;color:var(--text)}
.intro p{margin-bottom:17px}
.footer{left:25px;top:1056px;width:960px;border-top:1px solid var(--rule);padding-top:10px;display:flex;font-size:10.5px}
.footer a{color:var(--link);text-decoration:none;margin-right:30px}
.footer .copy{margin-left:auto;color:var(--muted)}
</style>
</head>
<body>
<div class="page">
  <div class="abs brand"><span class="brand-mark"></span><span>Patrons of the Northern Heritage Hall</span></div>

  <nav class="abs util-nav">
    <a href="#">Contact</a><a href="#">Related Sites</a><a href="#">Donate</a><a href="#">Sitemap</a><a href="#">Français</a><a href="#">Member Login</a>
  </nav>

  <div class="abs font-size">Font Size <a href="#" style="font-size:11px">A-</a><a href="#" style="font-size:13px">A</a><a href="#" style="font-size:15px">A+</a></div>
  <a class="abs social red" href="#" aria-label="Video channel"></a>
  <a class="abs social blue" href="#" aria-label="Social page"></a>
  <div class="abs search">
    <svg width="16" height="16" viewBox="0 0 16 16" aria-hidden="true"><circle cx="9.5" cy="6.5" r="4.5" fill="none" stroke="#4a8ab5" stroke-width="2"/><line x1="6.3" y1="9.7" x2="2" y2="14" stroke="#4a8ab5" stroke-width="2.5" stroke-linecap="round"/></svg>
  </div>

  <nav class="abs tabs main-nav">
    <a class="active" href="#" style="width:75px">Home</a>
    <a href="#" style="width:80px">About</a>
    <a href="#" style="width:139px">Support PNHH</a>
    <a href="#" style="width:84px">Events</a>
    <a href="#" style="width:176px">Projects &amp; Programs</a>
    <a href="#" style="width:151px">Meet the Friends</a>
    <a href="#" style="width:110px">Volunteers</a>
    <a href="#" style="width:121px">Publications</a>
  </nav>

  <div class="abs frame hero">
    <div class="abs hero-photo" role="img" aria-label="Exterior photo of the heritage hall building with its angled roof and plaza at dusk"></div>
  </div>

  <nav class="abs tabs join-tabs">
    <a class="active" href="#" style="width:120px">Be a Friend</a>
    <a href="#" style="width:110px">Be a Donor</a>
    <a href="#" style="width:139px">Be a Volunteer</a>
  </nav>

  <div class="abs frame feature">
    <div class="abs feature-photo" role="img" aria-label="Vintage four-engine bomber aircraft in flight over green fields"></div>
  </div>

  <div class="abs intro">
    <p>Lorem ipsum dolor sit amet, his laoreet theophrastus ut, id eum sententiae persequeris, diceret inimicus scriptorem cu nec. Te quo utroque albucius constituam, mei et duis iracundia, at est probo decore aperiri. Aperiam meliore molestie ei eos, facer nullam per ad, no sanctus pericula vix. Ea aeque mucius offendit sea, justo alterum pro ut, at percipit accommodare vel.</p>
    <p>Sea cu solet suavitate, et solum placerat vix. Te pro alienum sadipscing ullamcorper, summo exerci appetere ne usu, pro ei diam aliquip meliore. Ad nostrud reprimique mea, integre elaboraret referrentur ius cu. Graece iisque sententiae an vel. Alia possit ut qui, erroribus suscipiantur ea eam.</p>
    <p>Tibique corpora senserit pro ad, delicata disputationi sea ex. In modus voluptatibus pri, nam eu liber causae</p>
  </div>

  <footer class="abs footer">
    <a href="#">Home</a><a href="#">About</a><a href="#">Support PNHH</a><a href="#">Events</a><a href="#">Projects &amp; Programs</a><a href="#">Meet the Friends</a><a href="#">Volunteers</a><a href="#">Publications</a>
    <span class="copy">Copyright © PNHH</span>
  </footer>
</div>
</body>
</html>
```